New Graphic Design Project / Email signiture and Letterhead

I would like a new SIMPLE but high end quality modern/heavy industrial design for an email Signiture and letter head that incorporates product photos or illustrations of our products to show our customers our range of products and also show our head office in Perth Western Australia and also our Australian and international reseller locations.
in my present email signature you would see that I have other company logos these companies are old partners of ours but some are no longer so I would like to have the option to add and change them if things change in the future.
for ideas Our main products are as follows
Composite Hose
Convoluted hose
Metal expansion joints
Fabric expansion joints
Rubber Expansion joints
Please see our website for ideas and our product photos.
www.brovantec.com.au
if you need any further information please let me know
i have attached our old email signiture for reference.
Declan

Target Market(s)

Oil and Gas / Mining / Petroleum and Chemical Refineries, high end engineering

Requirements
Must have
• pictures / photos of our core products and our company capabilities to show our existing and new customers what we can do.
in the email signature - links to company face book and LinkedIn, our website
I would like to have spaces for my company partners logos and need the final file to be in a format for me to change and update all details
All so our Font is Conthrax SB
Nice to have
• the email signature, I would like this to have all the required information ( as per attached present email signature ) but also be informative / marketing to show customers what we do if possible.
the letter head can be based from the same but simple with or without product photos

```html
<!DOCTYPE html>
<html lang="en">
<head>
<meta charset="utf-8">
<title>Brovantec Letterhead and Email Signature</title>
<link href="https://fonts.googleapis.com/css2?family=Roboto:wght@300;400;500&display=swap" rel="stylesheet">
<style>
  :root{
    --bg:#ffffff;
    --ink:#3a3a3a;
    --ink-soft:#6d6d6d;
    --rule:#d4d4d4;
    --accent:#1e88e5;
    --brand:#2b2b2b;
    --art-a:#f4f6f8;
    --art-b:#e9edf1;
    --badge:#e3e6ea;
    --social:#4a8fd6;
  }
  *{margin:0;padding:0;box-sizing:border-box}
  html,body{width:681px;height:1200px;overflow:hidden;background:var(--bg)}
  body{position:relative;font-family:"Roboto",Arial,sans-serif;color:var(--ink)}

  .letterhead{position:absolute;left:57px;top:42px;width:566px;height:800px;background:#fff;
    box-shadow:0 4px 18px rgba(0,0,0,.18)}
  .brand{display:flex;align-items:center;gap:8px;font-weight:500;color:var(--brand);letter-spacing:2px}
  .brand-mark{width:26px;height:26px;border:2px solid var(--brand);border-radius:50%}
  .letterhead .brand{position:absolute;top:48px;left:50%;transform:translateX(-50%);font-size:22px}
  .letterhead-art{position:absolute;left:110px;top:330px;width:346px;height:360px;
    background:radial-gradient(ellipse at 50% 55%,var(--art-b),var(--art-a) 60%,#fff 100%)}
  .letterhead-footer{position:absolute;left:0;right:0;top:728px;text-align:center;font-size:8px;line-height:13px;color:var(--ink-soft)}
  .letterhead-footer::before{content:"";display:block;width:46px;height:2px;background:var(--accent);margin:0 auto 12px}

  .signature{position:absolute;left:45px;top:900px;width:591px;height:236px;background:#fff;
    box-shadow:0 3px 14px rgba(0,0,0,.18)}
  .signature .brand{position:absolute;left:22px;top:32px;font-size:20px}
  .sig-products{position:absolute;left:22px;top:86px;width:210px;height:36px;border-radius:3px;
    background:linear-gradient(90deg,#56606b,#8c96a0,#3d4652,#7a838c)}
  .sig-divider{position:absolute;left:250px;top:20px;width:1px;height:140px;background:var(--rule)}
  .sig-name{position:absolute;left:268px;top:20px;font-size:22px;font-weight:400;color:#555}
  .sig-role{position:absolute;left:268px;top:48px;font-size:10px;letter-spacing:2.5px;color:var(--ink-soft)}
  .sig-social{position:absolute;left:468px;top:26px;display:flex;gap:8px}
  .sig-social span{width:13px;height:13px;background:var(--social);border-radius:2px}
  .sig-social span:nth-child(2){background:#7fb06a}
  .sig-social span:nth-child(3){background:#d76a6a}
  .sig-contacts{position:absolute;left:268px;top:78px;display:grid;grid-template-columns:130px 150px;row-gap:6px;font-size:8.5px;color:var(--ink)}
  .sig-contacts div{display:flex;align-items:center;gap:6px}
  .sig-contacts svg{width:9px;height:9px;fill:var(--ink-soft)}
  .sig-regions{position:absolute;left:268px;top:138px;font-size:8.5px;color:var(--ink-soft);word-spacing:4px}
  .sig-partners{position:absolute;left:14px;top:178px;width:563px;display:flex;gap:8px;padding-top:12px;border-top:1px solid var(--rule)}
  .sig-partners span{flex:1;height:30px;background:var(--badge);border-radius:2px}
</style>
</head>
<body>

<section class="letterhead">
  <div class="brand"><span class="brand-mark"></span>BROVANTEC</div>
  <div class="letterhead-art" role="img" aria-label="Faint line illustration of two engineers in hard hats reviewing plans"></div>
  <div class="letterhead-footer">
    24 Kestrel Road Welshpool, WA 6106<br>
    Phone: +61 8 9400 1234 &nbsp;·&nbsp; +61 8 9400 5678<br>
    Web: www.brovantec.com.au
  </div>
</section>

<section class="signature">
  <div class="brand"><span class="brand-mark"></span>BROVANTEC</div>
  <div class="sig-products" role="img" aria-label="Row of product photos: hoses and expansion joints"></div>
  <div class="sig-divider"></div>

  <div class="sig-name">Declan Marsh</div>
  <div class="sig-role">Managing Director</div>
  <div class="sig-social"><span></span><span></span><span></span><span></span></div>

  <div class="sig-contacts">
    <div><svg viewBox="0 0 10 10"><path d="M2 1l2 2-1 1.5c.8 1.4 1.6 2.2 3 3L7.5 6l2 2-1.5 1.5C4.5 9 1 5.5.5 2z"/></svg>+61 8 9400 1234</div>
    <div><svg viewBox="0 0 10 10"><circle cx="5" cy="5" r="4.5"/></svg>www.brovantec.com.au</div>
    <div><svg viewBox="0 0 10 10"><rect x="1" y="0.5" width="8" height="9" rx="1"/></svg>+61 8 9400 5678</div>
    <div><svg viewBox="0 0 10 10"><path d="M5 0a3.5 3.5 0 0 1 3.5 3.5C8.5 6 5 10 5 10S1.5 6 1.5 3.5A3.5 3.5 0 0 1 5 0z"/></svg>24 Kestrel Road</div>
    <div><svg viewBox="0 0 10 10"><path d="M0 2h10v6H0z"/></svg>declan@brovantec.com.au</div>
    <div style="padding-left:15px">Welshpool, WA 6106</div>
  </div>
  <div class="sig-regions">Australia | Singapore | Indonesia | Vietnam</div>

  <div class="sig-partners">
    <span></span><span></span><span></span><span></span><span></span><span></span><span></span><span></span><span></span>
  </div>
</section>

</body>
</html>
```